Evening of Discovery Annual Fundraising Dinner

I need a design for an invitation to our Evening of Discovery fundraising dinner.
The organization is called Halvern Joint Science Trust Foundation. (Find info at movewellfund.example)
Our organization tries to raise money to fund research into arthritis - all the different kinds of arthritis. We fund cutting edge research by giving grants to young scientists at different universities . I'm looking for an innovative design for the invitation to this event .
At this event we introduce our audience to to Scientists that we gave grants to in the previous year and tell them about the scientists who applied for grants this year. We also use the event to raise money towards these grants

Target Market(s)

Adults who suffer from Arthritis or who have relatives who suffer from arthritis and who want to learn more about the research being done to try to find a cure and who are willing to donate towards the cause

Industry/Entity Type

Foundation

Font styles to use
Sans Serif

Colors
ed2a32
0355a3

Requirements
Should not have
• We are NOT the Corlane Health Society we are a REsearch foundation .... Raising money for research .

```html
<!DOCTYPE html>
<html lang="en">
<head>
<meta charset="utf-8">
<title>Evening of Discovery Annual Fundraising Dinner</title>
<link rel="stylesheet" href="https://fonts.googleapis.com/css2?family=Bebas+Neue&family=Roboto+Condensed:wght@300;400&display=swap">
<style>
  :root {
    --red: #ed2a32;
    --red-deep: #a3121c;
    --blue: #0355a3;
    --ink: #2d3037;
    --paper: #f2f2f2;
    --body-grey: #6b6b6b;
    --footer-text: #c9ccd2;
    --backdrop: #e7e4df;
    --white: #ffffff;
  }
  * { margin: 0; padding: 0; box-sizing: border-box; }
  html, body { width: 1044px; height: 1200px; overflow: hidden; }
  body {
    background: var(--backdrop);
    font-family: "Roboto Condensed", "Arial Narrow", sans-serif;
    position: relative;
  }
  .invitation {
    position: absolute;
    left: 69px; top: 43px;
    width: 906px; height: 1115px;
    display: flex; flex-direction: column;
    background: var(--paper);
    box-shadow: 0 6px 18px rgba(0,0,0,0.18);
  }
  .header {
    height: 170px;
    background: linear-gradient(90deg, var(--red) 0%, var(--red) 45%, var(--red-deep) 100%);
    color: var(--white);
    text-align: center;
    padding-top: 44px;
  }
  .title {
    font-family: "Bebas Neue", sans-serif;
    font-weight: 400;
    font-size: 50px;
    letter-spacing: 0.5px;
    line-height: 1;
  }
  .tagline {
    font-family: "Bebas Neue", sans-serif;
    font-size: 23px;
    margin-top: 18px;
    letter-spacing: 0.3px;
  }
  .hero-photo {
    height: 412px;
    background: linear-gradient(100deg, #d9d9d9 0%, #f4f4f4 30%, #bdbdbd 55%, #eeeeee 80%, #dcdcdc 100%);
  }
  .event-details {
    height: 136px;
    background: var(--blue);
    color: var(--white);
    text-align: center;
    font-size: 23px;
    padding-top: 13px;
  }
  .event-date { line-height: 1.3; }
  .divider {
    width: 642px; height: 2px;
    background: var(--white);
    margin: 13px auto 12px;
  }
  .venue, .address { line-height: 1.25; }
  .mission {
    height: 234px;
    text-align: center;
    padding-top: 26px;
  }
  .mission-heading {
    font-family: "Bebas Neue", sans-serif;
    color: var(--red);
    font-size: 31px;
    letter-spacing: 0.3px;
    line-height: 1;
  }
  .mission-text {
    color: var(--body-grey);
    font-size: 20.5px;
    font-weight: 300;
    line-height: 1.3;
    margin: 20px auto 0;
    width: 780px;
  }
  .footer {
    flex: 1;
    background: var(--ink);
    display: flex;
    align-items: center;
    justify-content: space-between;
    padding: 0 52px 0 46px;
  }
  .contact { list-style: none; }
  .contact li {
    display: flex; align-items: center; gap: 10px;
    font-family: "Bebas Neue", sans-serif;
    color: var(--footer-text);
    font-size: 24px;
    letter-spacing: 1.5px;
    line-height: 1;
  }
  .contact li + li { margin-top: 18px; }
  .contact svg { width: 18px; height: 18px; flex: none; }
  .brand {
    display: flex; flex-direction: column; align-items: center; gap: 8px;
  }
  .brand-dot {
    width: 64px; height: 64px; border-radius: 50%;
    background: var(--blue);
  }
  .brand-name {
    font-family: "Bebas Neue", sans-serif;
    color: var(--red);
    font-size: 22px;
    line-height: 1.05;
    text-align: center;
    letter-spacing: 0.8px;
  }
</style>
</head>
<body>
  <main class="invitation">
    <header class="header">
      <h1 class="title">Evening of Discovery Annual Fundraising Dinner</h1>
      <p class="tagline">Please join us in the effort to cure arthritis!</p>
    </header>

    <div class="hero-photo" role="img" aria-label="Black and white photograph of two scientists in lab coats and safety goggles, one looking into a microscope"></div>

    <section class="event-details">
      <p class="event-date">April 5, 2017 at 6:00pm</p>
      <div class="divider"></div>
      <p class="venue">LARKSPUR HALL MERIDIAN COMMONS</p>
      <p class="address">418 Meridian Plaza Drive, Garden Level Halden, CA 90210</p>
    </section>

    <section class="mission">
      <h2 class="mission-heading">Make a donation // Many ways to make a difference</h2>
      <p class="mission-text">Mission: To provide initial research funding to brilliant, investigative scientists with new ideas to cure arthritis and related autoimmune diseases.<br>With 91 cents of every dollar placed directly into arthritis research programs, the Halvern Joint Science Trust Foundation is committed to research and being good stewards of our donor funds.</p>
    </section>

    <footer class="footer">
      <ul class="contact">
        <li>
          <svg viewBox="0 0 24 24" aria-hidden="true"><path fill="#c9ccd2" d="M6.6 10.8a15.1 15.1 0 0 0 6.6 6.6l2.2-2.2a1 1 0 0 1 1-.25 11.4 11.4 0 0 0 3.6.57 1 1 0 0 1 1 1V20a1 1 0 0 1-1 1A17 17 0 0 1 3 4a1 1 0 0 1 1-1h3.5a1 1 0 0 1 1 1c0 1.25.2 2.45.57 3.57a1 1 0 0 1-.25 1z"/></svg>
          555.014.2290
        </li>
        <li>
          <svg viewBox="0 0 24 24" aria-hidden="true"><g fill="none" stroke="#c9ccd2" stroke-width="1.6"><circle cx="12" cy="12" r="9.5"/><ellipse cx="12" cy="12" rx="4.2" ry="9.5"/><path d="M2.5 12h19M4 7h16M4 17h16"/></g></svg>
          movewellfund.example
        </li>
      </ul>
      <div class="brand">
        <div class="brand-dot" aria-hidden="true"></div>
        <p class="brand-name">Halvern Joint Science<br>Trust Foundation</p>
      </div>
    </footer>
  </main>
</body>
</html>
```